Letterhead

We are looking for a basic letterhead. It should include our logo, website - northpeakkitchenware.com, phone 907.418.3952, toll free 855.392.6180, and fax 907.418.5263, along with our address 4837 Birchwood Lane, Anchorage, AK 99517. I want something that will look good printed in color or black and white.

```html
<!DOCTYPE html>
<html lang="fr">
<head>
<meta charset="utf-8">
<title>North Peak Kitchenware – Letterhead</title>
<link href="https://fonts.googleapis.com/css2?family=Source+Sans+3:wght@400;600&family=Montserrat:wght@700;800&display=swap" rel="stylesheet">
<style>
  :root {
    --backdrop: #e6e7e8;
    --paper: #ffffff;
    --brand-red: #c1323f;
    --brand-red-fade: rgba(193, 50, 63, 0);
    --brand-navy: #1c3f7a;
    --ink: #474747;
    --signature-tone: #ececec;
  }
  * { margin: 0; padding: 0; box-sizing: border-box; }
  html, body { width: 1200px; height: 900px; overflow: hidden; }
  body { background: var(--backdrop); position: relative; font-family: "Source Sans 3", Arial, sans-serif; }

  .letterhead {
    position: absolute; left: 334px; top: 72px;
    width: 531px; height: 753px;
    background: var(--paper); overflow: hidden;
  }
  .corner-accent { position: absolute; }
  .corner-accent--top {
    left: 0; top: 0; width: 240px; height: 110px;
    background: radial-gradient(ellipse at top left, var(--brand-red) 0%, rgba(193, 50, 63, 0.55) 40%, var(--brand-red-fade) 75%);
  }
  .corner-accent--bottom {
    right: 0; bottom: 0; width: 300px; height: 110px;
    background: radial-gradient(ellipse at bottom right, var(--brand-red) 0%, rgba(193, 50, 63, 0.55) 40%, var(--brand-red-fade) 75%);
  }

  .company-name {
    position: absolute; right: 42px; top: 58px;
    text-align: right; color: var(--brand-navy);
    font-family: "Montserrat", Arial, sans-serif; font-weight: 800;
    font-size: 21px; line-height: 24px; letter-spacing: 0.5px; text-transform: uppercase;
  }

  .letter-body {
    position: absolute; left: 55px; top: 187px; width: 416px;
    color: var(--ink); font-size: 10.6px; line-height: 12.6px; font-weight: 600;
  }
  .recipient { margin-bottom: 25px; }
  .salutation { margin-bottom: 27px; }
  .letter-body p.paragraph { text-indent: 33px; margin-bottom: 12.6px; }
  .closing { margin-top: 20px; }

  .signature-area {
    position: absolute; left: 55px; top: 590px; width: 96px; height: 36px;
  }
  .signature-mark { position: absolute; left: 6px; top: 0; width: 62px; height: 32px; background: var(--signature-tone); border-radius: 4px; }
  .signature-line { position: absolute; left: 0; bottom: 2px; width: 96px; border-bottom: 1px dotted var(--ink); }

  .contact-footer {
    position: absolute; left: 50px; top: 677px;
    color: var(--brand-red); font-family: "Montserrat", Arial, sans-serif; font-weight: 700;
  }
  .contact-footer .address { font-size: 10.5px; line-height: 13px; }
  .contact-footer .detail { font-size: 8px; line-height: 11px; }
</style>
</head>
<body>
  <main class="letterhead">
    <div class="corner-accent corner-accent--top" role="img" aria-label="Decorative red corner swoosh"></div>

    <div class="company-name">North Peak<br>Kitchenware</div>

    <section class="letter-body">
      <p class="recipient">13-02-2014<br>Nalin Perera<br>Greenhill Estate,<br>Kandapola<br>Sri lanka</p>
      <p class="salutation">Dear Sir,</p>
      <p class="paragraph">La rencontre était censée être un événement décisif pour le Nigeria alors que le pays a été classé comme la première économie africaine.Mais l'inquiétude est palpable dans la capitale après les récentes attaques menées par Boko Haram.Après une journée de rencontres privées, le forum</p>
      <p class="paragraph">Il est accompagné d'une importante délégation d'hommes d'affaires pour une tournée africaine.Au total, les organisateurs de l'événement s'attendent à la participation de plus de 70 pays d'Afrique. Toutefois, le forum a lieu dans une atmosphère dominée par les préoccupations sécuritaires. La capitale Abuja a récemment été secouée par une double explosion qui a fait des dizaines de victimes. L'attentat a été attribué aux militants de Boko Haram qui ont revendiqué l'enlèvement de près de 200 lycéennes dans le nord du pays. Les organisateurs assurent qu'ils ont pris les mesures nécessaires pour assurer la sécurité des participants au foru</p>
      <p class="paragraph">Mais des investisseurs se disent prêt à ignorer certains risques sécuritaires à cause des opportunités commerciales que le Nigeria peut offrir notamment dans les secteurs comme le pétrole, le gaz et l'électricité.)revendiqué l'enlèvement de près de 200 d'écoliers par des groupes armés dans plusieurs régions isolées du pays, selon les autorités locales qui poursuivent leurs recherches sans relâche depuis ycéennes dans le nord du pays. Les.</p>
      <p class="closing">Your Signature</p>
    </section>

    <div class="signature-area">
      <div class="signature-mark" role="img" aria-label="Handwritten signature"></div>
      <div class="signature-line"></div>
    </div>

    <footer class="contact-footer">
      <p class="address">4837 Birchwood Lane, Anchorage, AK 99517</p>
      <p class="detail">Phone : 907.418.3952 | Toll free : 855.392.6180</p>
      <p class="detail">Fax : 907.418.5263</p>
      <p class="detail">www. northpeakkitchenware.com</p>
    </footer>

    <div class="corner-accent corner-accent--bottom" role="img" aria-label="Decorative red corner swoosh"></div>
  </main>
</body>
</html>
```